Kerrow Supply Website Redesign

Currently kerrowsupply.example is focussed on fulfillment and transport from various products in the BBQ segment. However, no we want to update our business activities to Product Development, Brand Development, Online Positioning, Logistics & Aftersales, and Promotional BBQs. We will be a business for Outdoor Leisure Development from A to Z.

Therefore, we need a brand new website. The colours of the current website may be the same. However, i'd like to keep it clean. More white and use blue and green as accent colours. It is a business to business organization so the website should be looking formal and corporate. However we sell fun products so not too formal and corporate.

Pages we need; Home, About, Contact, Our Services (+ page per service) a place to share our news/blogs.

I have added some sort of mock up of an idea. However it needs some finetuning.

Target Market(s)

Businesses

Industry/Entity Type

Corporate/Logistics/Marketing

Coding

Coded - Design and coding required

Colors

Designer to choose colors to be used in the design.

Requirements
Must have
• Show clear distinguishing of the different services we provide (Product Development, Brand Development, Online Positioning, Logistics & Aftersales and Promotional BBQs). Every service should have its own page too. Besides, I would like to have a blog page to share relevant content.
Nice to have
• Show that we are the expert in Outdoor LEisure Development from A to Z
Should not have
• Be too informal. It may be semi-formal

```html
<!DOCTYPE html>
<html lang="en">
<head>
<meta charset="utf-8">
<title>Kerrow Supply – Outdoor Leisure Development From A to Z</title>
<link href="https://fonts.googleapis.com/css2?family=Outfit:wght@300;400;500;600;700&family=Roboto:wght@400;500&display=swap" rel="stylesheet">
<style>
:root{
  --green:#43b14b;
  --green-dark:#3a9e42;
  --teal:#0fb8b0;
  --slate:#37606f;
  --ink:#2b3236;
  --text:#3d4448;
  --muted:#6b7478;
  --mist:#e9edef;
  --line:#e3e6e8;
  --footer:#1e1f20;
  --white:#ffffff;
}
*{box-sizing:border-box;margin:0;padding:0}
html,body{width:1200px;height:2688px;overflow:hidden;background:var(--white)}
body{font-family:"Outfit",sans-serif;color:var(--text);position:relative}
.abs{position:absolute}
a{color:inherit;text-decoration:none}

/* top bar */
.topbar{left:0;top:0;width:1200px;height:43px;background:linear-gradient(90deg,#2bb36a,var(--teal));color:var(--white);font-family:"Roboto",sans-serif;font-size:12px}
.topbar .item{position:absolute;top:13px;display:flex;align-items:center;gap:5px}
.topbar .dot{width:9px;height:9px;border-radius:50%;background:rgba(255,255,255,.85);position:absolute;top:17px}

/* header */
.header{left:0;top:43px;width:1200px;height:80px;background:var(--white)}
.brand{position:absolute;display:flex;align-items:center;gap:10px;font-weight:700;color:var(--slate)}
.brand .mark{border-radius:50%;background:var(--green)}
.header .brand{left:158px;top:20px;font-size:34px}
.header .brand .mark{width:26px;height:26px}
.nav{position:absolute;top:32px;font-family:"Roboto",sans-serif;font-size:14px;color:var(--ink);letter-spacing:.2px}
.nav.active{color:var(--green)}

/* hero */
.hero{left:0;top:123px;width:1200px;height:408px;background:linear-gradient(100deg,#eceeef 0%,#dcdfe0 45%,#c7cacb 58%,#e3e5e6 75%,#e9ebec 100%);overflow:hidden}
.hero .blob{position:absolute;left:838px;top:188px;width:420px;height:420px;border-radius:50%;background:#d7dadc}
.hero .kicker{position:absolute;left:158px;top:84px;font-size:32px;font-weight:300;color:var(--green)}
.hero h1{position:absolute;left:157px;top:118px;font-size:60px;line-height:62px;font-weight:700;color:var(--slate)}
.btn{position:absolute;background:var(--green);color:var(--white);font-family:"Roboto",sans-serif;font-weight:500;display:flex;align-items:center;justify-content:center;text-transform:uppercase}
.hero .btn{left:160px;top:263px;width:165px;height:50px;font-size:14px}
.pager{position:absolute;left:165px;top:359px;display:flex;gap:13px}
.pager span{width:11px;height:11px;background:#a8b6bc}
.pager span.on{background:var(--slate)}

/* services */
.service{top:569px;width:280px;height:198px;background:var(--white);box-shadow:0 4px 18px rgba(0,0,0,.09);text-align:center}
.service .icon{position:absolute;left:95px;top:25px;width:90px;height:90px;border-radius:8px;background:#e3f3e4}
.service h3{position:absolute;left:0;width:100%;top:144px;font-size:22px;font-weight:600;color:var(--ink)}
.service.featured{background:var(--green);color:var(--white)}
.service.featured .icon{left:113px;top:16px;width:54px;height:54px;background:rgba(255,255,255,.25)}
.service.featured h3{top:78px;color:var(--white)}
.service.featured p{position:absolute;left:30px;width:220px;top:113px;font-size:14px;line-height:23px}
.chev{position:absolute}

/* welcome */
.ring-left{left:-110px;top:985px;width:246px;height:246px;border-radius:50%;background:var(--mist)}
.ring-right{left:946px;top:890px;width:120px;height:120px;border-radius:50%;background:var(--slate)}
.welcome h2{position:absolute;left:160px;top:874px;font-size:50px;font-weight:600;color:var(--ink)}
.welcome h2 em{font-style:normal;color:var(--green)}
.welcome p{position:absolute;left:160px;top:944px;width:425px;font-size:15.5px;line-height:24.5px}
.checks{position:absolute;left:160px;top:1026px;list-style:none;font-size:15.5px}
.checks li{display:flex;align-items:center;gap:8px;height:35px}
.welcome .btn{left:160px;top:1146px;width:165px;height:50px;font-size:14px}
.ship{left:622px;top:885px;width:418px;height:313px;background:linear-gradient(135deg,#2e6f9c 0%,#2879a8 40%,#6d8fa6 70%,#b59aa4 100%)}

/* difference band */
.band{left:0;top:1278px;width:1200px;height:389px;background:linear-gradient(100deg,#2fa35c 0%,#27b389 50%,#2cc0b2 100%);color:var(--white);text-align:center}
.band h2{position:absolute;left:0;width:100%;top:100px;font-size:48px;font-weight:600}
.band p{position:absolute;left:235px;width:730px;top:170px;font-size:15.5px;line-height:24.5px;font-weight:500}

/* news */
.news-head{left:0;width:1200px;top:1708px;text-align:center}
.news-head h2{font-size:50px;font-weight:600;color:var(--ink)}
.news-head p{width:520px;margin:8px auto 0;font-size:15.5px;line-height:23px;color:var(--ink)}
.card{top:1851px;width:281px;height:409px;background:var(--white);box-shadow:0 3px 14px rgba(0,0,0,.1)}
.card .photo{height:181px}
.card .date{position:absolute;left:23px;top:201px;font-size:11.5px;color:var(--muted);display:flex;align-items:center;gap:5px}
.card h4{position:absolute;left:23px;top:222px;width:240px;font-size:15px;line-height:19px;font-weight:600;color:var(--ink)}
.card p{position:absolute;left:23px;top:273px;width:240px;font-size:12.5px;line-height:21px;color:var(--text)}
.card .btn{left:23px;top:343px;width:124px;height:38px;font-size:11px}
.round{position:absolute;width:46px;height:46px;border-radius:50%;display:flex;align-items:center;justify-content:center}

/* footer */
.footer{left:0;top:2329px;width:1200px;height:359px;background:var(--footer);color:#bfc3c5}
.footer .brand{left:160px;top:88px;font-size:60px;color:var(--slate)}
.footer .brand .mark{width:38px;height:38px}
.socials{position:absolute;left:160px;top:196px;display:flex;gap:30px}
.socials span{width:16px;height:16px;border-radius:50%;background:#e8e8e8}
.copy{position:absolute;left:163px;top:266px;font-size:14px;color:#9a9fa2}
.copy b{font-weight:400;color:var(--green)}
.col{position:absolute;top:85px}
.col h5{font-size:21px;font-weight:500;color:var(--green);margin-bottom:12px}
.col a{display:block;font-size:14.5px;color:#c8cccd}
.col.sitemap a{height:43px}
.col.services a{height:36px}
.contact-row{display:flex;gap:10px;font-size:14.5px;line-height:25px;color:#c8cccd;margin-bottom:12px}
.contact-row svg{flex:none;margin-top:5px}
</style>
</head>
<body>

<div class="abs topbar">
  <div class="item" style="left:165px">
    <svg width="10" height="10" viewBox="0 0 24 24"><path fill="#fff" d="M6.6 10.8a15 15 0 0 0 6.6 6.6l2.2-2.2a1 1 0 0 1 1-.25 11.4 11.4 0 0 0 3.6.6 1 1 0 0 1 1 1V20a1 1 0 0 1-1 1A17 17 0 0 1 3 4a1 1 0 0 1 1-1h3.5a1 1 0 0 1 1 1c0 1.25.2 2.45.6 3.6a1 1 0 0 1-.25 1z"/></svg>
    (+31) 20 555 0148</div>
  <div class="item" style="left:314px">
    <svg width="11" height="8" viewBox="0 0 22 16"><rect width="22" height="16" rx="2" fill="#fff"/><path d="M1 1l10 8 10-8" stroke="#27b38a" stroke-width="2" fill="none"/></svg>
    info@kerrowsupply.example</div>
  <div class="item" style="left:904px">Follow Us:</div>
  <span class="dot" style="left:974px"></span>
  <span class="dot" style="left:1000px"></span>
  <span class="dot" style="left:1029px"></span>
</div>

<header class="abs header">
  <div class="brand"><span class="mark"></span>Kerrow Supply</div>
  <a class="nav active" style="left:674px">HOME</a>
  <a class="nav" style="left:752px">ABOUT</a>
  <a class="nav" style="left:836px">OUR SERVICES</a>
  <a class="nav" style="left:972px">CONTACT</a>
</header>

<section class="abs hero">
  <div role="img" aria-label="Photo of a man pointing forward, his portrait blended with a city skyline" style="position:absolute;left:390px;top:0;width:470px;height:408px;background:linear-gradient(90deg,rgba(200,200,200,0) 0%,#b9bcbd 30%,#8f8c88 55%,#b8bbbc 80%,rgba(200,200,200,0) 100%)"></div>
  <div class="blob"></div>
  <div class="kicker">Outdoor Leisure</div>
  <h1>Development<br>From A to Z</h1>
  <a class="btn">Contact Us</a>
  <div class="pager"><span class="on"></span><span></span><span></span></div>
</section>

<svg class="chev" style="left:152px;top:653px" width="16" height="30" viewBox="0 0 16 30"><path d="M14 2L2 15l12 13" stroke="#555" stroke-width="1.5" fill="none"/></svg>
<svg class="chev" style="left:1036px;top:653px" width="16" height="30" viewBox="0 0 16 30"><path d="M2 2l12 13L2 28" stroke="#555" stroke-width="1.5" fill="none"/></svg>

<div class="abs service" style="left:160px">
  <div class="icon" role="img" aria-label="Line icon of a blueprint with a box and drafting tools"></div>
  <h3>Product Development</h3>
</div>
<div class="abs service featured" style="left:461px">
  <div class="icon" role="img" aria-label="Line icon of a hand holding a rocket"></div>
  <h3>Brand Development</h3>
  <p>Lorem ipsum dolor sit amsectetur adipiscing elit, sed do eiusmod tempor</p>
</div>
<div class="abs service" style="left:763px">
  <div class="icon" role="img" aria-label="Line icon of boxes on a conveyor belt with a robotic arm"></div>
  <h3>Logistics &amp; Aftersales</h3>
</div>

<div class="abs ring-left"></div>
<div class="abs ring-right"></div>
<section class="welcome">
  <h2>Welcome to <em>Kerrow</em></h2>
  <p>Lorem ipsum dolor sit amet, consectetur adipiscing elit, sed do eiusmod tempor incididunt ut labore et dolore magna aliqua. Quis ipsum suspendisse ultrices grda.</p>
  <ul class="checks">
    <li><svg width="18" height="14" viewBox="0 0 18 14"><path d="M1 7l5 5L17 2" stroke="#43b14b" stroke-width="3" fill="none"/></svg>Lorem ipsum dolor</li>
    <li><svg width="18" height="14" viewBox="0 0 18 14"><path d="M1 7l5 5L17 2" stroke="#43b14b" stroke-width="3" fill="none"/></svg>Consectetur adipiscing</li>
    <li><svg width="18" height="14" viewBox="0 0 18 14"><path d="M1 7l5 5L17 2" stroke="#43b14b" stroke-width="3" fill="none"/></svg>Quis ipsum suspendisse</li>
  </ul>
  <a class="btn">Read More</a>
</section>
<div class="abs ship" role="img" aria-label="Aerial photo of a container ship loaded with colourful containers on blue sea"></div>

<section class="abs band" role="img" aria-label="Aerial photo of a logistics park with roads, tinted green and teal">
  <h2>We Make The Difference</h2>
  <p>Lorem ipsum dolor sit amet, consectetur adipiscing elit. Nam finibus sem venenatis, malesuada neque nec, accumsan magna. Fusce non lorem sodales, auctor neque nec, eleifend enim. Morbi ullamcorper erat neque, ut porttitor augue mollis hendrerit. Praesent at fermentum ex. Donec gravida nisl ullamcorper erat tempus vehicula.</p>
</section>

<div class="abs news-head">
  <h2>Latest News</h2>
  <p>Lorem ipsum dolor sit amet, consectetur adipiscing elit, sed do eiusmod tempor incididunt ut labor</p>
</div>

<article class="abs card" style="left:160px">
  <div class="photo" role="img" aria-label="Photo of two colleagues reviewing a tablet in an office" style="background:linear-gradient(135deg,#d9d4cc,#6e6660 60%,#3c3a3a)"></div>
  <div class="date"><svg width="10" height="10" viewBox="0 0 10 10"><rect x=".5" y="1.5" width="9" height="8" fill="none" stroke="#43b14b"/><path d="M.5 4h9" stroke="#43b14b"/></svg>October 12, 2021</div>
  <h4>Phasellus at vehic dui veibulum cursus elementum</h4>
  <p>In hac habitse platea dictumst. Integer vestibulum augue libero, eget rhoncus eros facilisis eu. Nulla facilisi.</p>
  <a class="btn">Read More</a>
</article>
<article class="abs card" style="left:460px">
  <div class="photo" role="img" aria-label="Photo of hands pointing at printed charts on a desk" style="background:linear-gradient(135deg,#3b4452,#c9d2dc 45%,#eef1f5)"></div>
  <div class="date"><svg width="10" height="10" viewBox="0 0 10 10"><rect x=".5" y="1.5" width="9" height="8" fill="none" stroke="#43b14b"/><path d="M.5 4h9" stroke="#43b14b"/></svg>October 12, 2021</div>
  <h4>Phasellus at vehic dui veibulum cursus elementum</h4>
  <p>In hac habitse platea dictumst. Integer vestibulum augue libero, eget rhoncus eros facilisis eu. Nulla facilisi.</p>
  <a class="btn">Read More</a>
</article>
<article class="abs card" style="left:760px">
  <div class="photo" role="img" aria-label="Photo of large white block letters on a wooden surface" style="background:linear-gradient(135deg,#8a8580,#d8d6d2 50%,#6f6a64)"></div>
  <div class="date"><svg width="10" height="10" viewBox="0 0 10 10"><rect x=".5" y="1.5" width="9" height="8" fill="none" stroke="#43b14b"/><path d="M.5 4h9" stroke="#43b14b"/></svg>October 12, 2021</div>
  <h4>Phasellus at vehic dui veibulum cursus elementum</h4>
  <p>In hac habitse platea dictumst. Integer vestibulum augue libero, eget rhoncus eros facilisis eu. Nulla facilisi.</p>
  <a class="btn">Read More</a>
</article>
<div class="round" style="left:137px;top:1948px;background:rgba(200,200,200,.6)"><svg width="10" height="18" viewBox="0 0 10 18"><path d="M9 1L1 9l8 8" stroke="#fff" stroke-width="1.5" fill="none"/></svg></div>
<div class="round" style="left:1024px;top:1948px;background:rgba(67,177,75,.75)"><svg width="10" height="18" viewBox="0 0 10 18"><path d="M1 1l8 8-8 8" stroke="#fff" stroke-width="1.5" fill="none"/></svg></div>

<footer class="abs footer">
  <div class="brand"><span class="mark"></span>Kerrow</div>
  <div class="socials"><span></span><span></span><span></span></div>
  <div class="copy">© 2021 <b>Kerrow Supply</b>. All right reserved</div>

  <div class="col sitemap" style="left:434px">
    <h5>Sitemap</h5>
    <a>Home</a><a>About</a><a>Our Services</a><a>Contact</a>
  </div>
  <div class="col services" style="left:592px">
    <h5>Services</h5>
    <a>Product Development</a><a>Brand Development</a><a>Online Positioning</a><a style="height:43px">Logistics &amp; Aftersales</a><a>Promotional BBQs</a>
  </div>
  <div class="col" style="left:795px">
    <h5>Contact Us</h5>
    <div class="contact-row"><svg width="12" height="15" viewBox="0 0 12 15"><path d="M6 0a6 6 0 0 1 6 6c0 4-6 9-6 9S0 10 0 6a6 6 0 0 1 6-6z" fill="#43b14b"/><circle cx="6" cy="6" r="2.2" fill="#1e1f20"/></svg><span>Lindenhof 12<br>4811 KT, Weststad<br>The Netherlands</span></div>
    <div class="contact-row"><svg width="14" height="14" viewBox="0 0 24 24"><path fill="#43b14b" d="M6.6 10.8a15 15 0 0 0 6.6 6.6l2.2-2.2a1 1 0 0 1 1-.25 11.4 11.4 0 0 0 3.6.6 1 1 0 0 1 1 1V20a1 1 0 0 1-1 1A17 17 0 0 1 3 4a1 1 0 0 1 1-1h3.5a1 1 0 0 1 1 1c0 1.25.2 2.45.6 3.6a1 1 0 0 1-.25 1z"/></svg><span>(+31) 20 555 0148</span></div>
    <div class="contact-row"><svg width="14" height="11" viewBox="0 0 22 16"><rect width="22" height="16" rx="2" fill="#43b14b"/><path d="M1 1l10 8 10-8" stroke="#1e1f20" stroke-width="2" fill="none"/></svg><span>info@kerrowsupply.example</span></div>
  </div>
</footer>

</body>
</html>
```